Business Card Re-Design

Consulting Company: To build a high performance organization, you need great leaders at all levels throughout your organization. The Northvale Talent Growth Studio engages, inspires, and educates current and future leaders to step beyond the ordinary and deliver exceptional results. This new breed of leaders will motivate your staff to leave the safety of complacency behind and come together to build an extraordinary organization. The current trend has been to ask our people to do more with fewer resources. People have been stepping up to the challenge, but more is required to ensure success with a new work paradigm. We work with your management team to build a successful strategy that will make your organization more effective. NTGS then supports your management team by providing a comprehensive set of proven services to empower your entire organization to successfully execute new strategies.Let NTGS help you optimize your organization’s individual and team performance today!

Target Market(s)

Federal, State and Local Government / Non profit

Industry/Entity Type

Management Consulting

Contact Information for Business Card

NTGS, inc (Northvale Talent Growth Studio) Optimizing Individual and Organizational Performance

Colors
fee18a
ec1f27
474747
fbf289

Requirements
Must have
• Professional and high quality feel

```html
<!DOCTYPE html>
<html lang="en">
<head>
<meta charset="utf-8">
<title>Northvale Talent Growth Studio – Business Card</title>
<link rel="stylesheet" href="https://fonts.googleapis.com/css2?family=Montserrat:wght@600;700&family=Arimo:wght@400&display=swap">
<style>
  :root {
    --paper: #ffffff;
    --ink-dark: #263334;
    --ink-mid: #474747;
    --figure-core: rgba(110, 110, 110, 0.55);
    --figure-edge: rgba(150, 150, 150, 0);
    --icon: #2f3a3b;
  }
  html, body {
    margin: 0;
    padding: 0;
    width: 702px;
    height: 1200px;
    overflow: hidden;
    background: var(--paper);
  }
  .card {
    position: relative;
    width: 702px;
    height: 1200px;
    background: var(--paper);
    overflow: hidden;
    font-family: "Arimo", Arial, sans-serif;
    color: var(--ink-dark);
  }

  /* Brand block */
  .brand {
    position: absolute;
    left: 192px;
    top: 118px;
    width: 330px;
    display: flex;
    align-items: flex-start;
    gap: 16px;
  }
  .brand-square {
    flex: none;
    width: 24px;
    height: 24px;
    margin-top: 12px;
    background: var(--ink-mid);
  }
  .brand-name {
    margin: 0;
    font-family: "Montserrat", Arial, sans-serif;
    font-weight: 700;
    font-size: 36px;
    line-height: 1.2;
    letter-spacing: 1px;
    text-transform: uppercase;
    color: var(--ink-mid);
  }
  .brand-name span { display: block; }

  /* Team silhouettes area */
  .team-figures {
    position: absolute;
    left: 110px;
    top: 444px;
    width: 490px;
    height: 500px;
    background:
      radial-gradient(ellipse 50% 48% at 50% 50%, var(--figure-core) 0%, rgba(120,120,120,0.4) 60%, var(--figure-edge) 100%);
  }

  /* Name band */
  .name-band {
    position: absolute;
    left: 0;
    top: 565px;
    width: 702px;
    height: 137px;
    background: var(--paper);
    text-align: center;
  }
  .person-name {
    margin: 40px 0 0;
    font-family: "Montserrat", Arial, sans-serif;
    font-weight: 700;
    font-size: 40px;
    letter-spacing: 8px;
    line-height: 1;
    color: var(--ink-dark);
  }
  .person-title {
    margin: 16px 0 0;
    font-family: "Montserrat", Arial, sans-serif;
    font-weight: 600;
    font-size: 18px;
    letter-spacing: 4px;
    line-height: 1;
    color: var(--ink-dark);
  }

  /* Contact lines */
  .contact {
    position: absolute;
    left: 0;
    width: 702px;
    display: flex;
    justify-content: center;
    align-items: center;
    color: var(--ink-dark);
    white-space: nowrap;
  }
  .contact svg { fill: var(--icon); flex: none; }
  .contact-mobile { top: 972px; height: 44px; font-size: 35px; letter-spacing: 2px; gap: 12px; }
  .contact-row { top: 1032px; height: 36px; font-size: 26px; letter-spacing: 1px; gap: 10px; }
  .contact-row .gap { width: 30px; }
  .contact-address { top: 1090px; height: 36px; font-size: 26px; letter-spacing: 1px; gap: 10px; }
</style>
</head>
<body>
<main class="card">
  <header class="brand">
    <span class="brand-square" aria-hidden="true"></span>
    <h1 class="brand-name"><span>Northvale Talent</span><span>Growth Studio</span><span>NTGS, inc</span></h1>
  </header>

  <div class="team-figures" role="img" aria-label="Soft silhouettes of four standing business people"></div>

  <section class="name-band">
    <p class="person-name">DANIEL R.HOLLIS</p>
    <p class="person-title">PRESIDENT / CEO</p>
  </section>

  <div class="contact contact-mobile">
    <svg width="22" height="36" viewBox="0 0 22 36" aria-hidden="true"><rect x="1.5" y="1.5" width="19" height="33" rx="3" fill="none" stroke="#2f3a3b" stroke-width="3"/><rect x="5" y="6" width="12" height="20"/><circle cx="11" cy="30" r="1.8"/></svg>
    <span>555.014.2280</span>
  </div>

  <div class="contact contact-row">
    <svg width="36" height="32" viewBox="0 0 36 32" aria-hidden="true"><path d="M9 2h18v8H9z" fill="none" stroke="#2f3a3b" stroke-width="2.5"/><path d="M3 10h30v14h-6v-6H9v6H3z" fill="none" stroke="#2f3a3b" stroke-width="2.5"/><path d="M9 18h18v12H9z" fill="none" stroke="#2f3a3b" stroke-width="2.5"/></svg>
    <span>555.014.2291</span>
    <span class="gap"></span>
    <svg width="36" height="24" viewBox="0 0 36 24" aria-hidden="true"><rect width="36" height="24" rx="2"/><path d="M13 10l5 4 5-4" fill="none" stroke="#fff" stroke-width="1.5"/></svg>
    <span>ntgs@mailbox.com</span>
  </div>

  <div class="contact contact-address">
    <svg width="34" height="32" viewBox="0 0 34 32" aria-hidden="true"><path d="M17 1L1 16h5v15h8v-9h6v9h8V16h5z"/></svg>
    <span>2140 Alder Grove Road Fairmont, MD20999</span>
  </div>
</main>
</body>
</html>
```